businesscard, flyer and membercard

--------------------------------------------------------------------------------------------------
design flyer :
- delivering format (jpg, pdf and original psd)
- there is a example how the flyers should look like
the text and logo should be the same as the exemple flyer, the creativity is yours.
- the design should have a back and front side.
File format : 15,0 cm x 21,2 cm
design membercard :
- there is example how the member-card should look like
the text and logo should be the same as the exemple membercard, the creativity is yours.
- the front side contains text and open space where for writing :
Naam ......
Dansstijlen ......
- the front side contains 12 circels horizontal at the line name at the end of the line "Salsa".
- the front side contains 12 circels horizontal at the line name at the end of the line "Bachata".
- the front side contains 12 circels horizontal at the line name at the end of the line "Kizomba".
- each horizontal line with circels contains a different kind of color/design.
- file format: 7,6 cm x 10,7 cm
Business card :
- there is example how the businesscard should look like
the text and logo should be the same as the exemple buisinesscard, the creativity is yours.
- the design should have a back a front side
File format : 8,7 cm x 5,7 cm

Target Market(s)

Dancing :Salsa, Bachata and Kizomba

Colors

Designer to choose colors to be used in the design.

Requirements
Must have
• same text as seen on the examples.
Nice to have
• see the examples as attachments
Should not have
• - REMOVE TEXT "KOV" from the design
• - REMOVE TEXT "Gratis Parkeren"

```html
<!DOCTYPE html>
<html lang="nl">
<head>
<meta charset="utf-8">
<title>Solara Dance Studio – flyer voor- en achterzijde</title>
<link rel="stylesheet" href="https://fonts.googleapis.com/css2?family=Russo+One&family=Archivo+Black&family=Rajdhani:wght@500;600;700&display=swap">
<style>
:root{
  --page:#e9e9eb;
  --ink-dark:#14060f;
  --plum:#3a0f2c;
  --wine:#6d1030;
  --flame:#d8261f;
  --amber:#f0a13a;
  --gold:#e3b542;
  --silver:#d9d9de;
  --white:#ffffff;
  --yellow:#ffe400;
  --red-text:#e5221c;
  --panel:rgba(20,8,18,.78);
}
*{margin:0;padding:0;box-sizing:border-box}
html,body{width:1200px;height:797px;overflow:hidden;background:var(--page)}
body{position:relative;font-family:"Rajdhani",sans-serif;color:var(--white)}
.flyer{position:absolute;top:47px;width:504px;height:703px;overflow:hidden;
  background:
    radial-gradient(circle at 30% 35%,rgba(216,38,31,.55),transparent 45%),
    radial-gradient(circle at 80% 55%,rgba(240,161,58,.35),transparent 40%),
    radial-gradient(circle at 60% 80%,rgba(109,16,48,.8),transparent 55%),
    linear-gradient(160deg,var(--plum),var(--ink-dark) 70%);
  box-shadow:0 6px 18px rgba(0,0,0,.25)}
.flyer--front{left:50px}
.flyer--back{left:653px}
.abs{position:absolute;line-height:1;white-space:nowrap}
.center{text-align:center;left:0;right:0}

.brand{position:absolute;top:60px;width:210px;display:flex;align-items:center;justify-content:center;gap:8px}
.brand__dot{width:12px;height:12px;border-radius:50%;background:var(--white)}
.brand__name{font-family:"Russo One",sans-serif;font-size:30px;letter-spacing:3px;color:var(--white)}
.brand__tag{position:absolute;top:100px;width:210px;text-align:center;font-size:6px;letter-spacing:1px;color:var(--silver)}

.photo{position:absolute;border-radius:4px}
.photo--couple{left:54px;top:13px;width:392px;height:312px;
  background:radial-gradient(ellipse at 55% 45%,rgba(230,60,60,.75),rgba(120,40,40,.45) 45%,transparent 72%)}
.photo--pair{left:391px;top:437px;width:104px;height:224px;
  background:radial-gradient(ellipse at 50% 45%,rgba(210,30,40,.8),rgba(60,20,30,.3) 60%,transparent 78%)}

.splash{position:absolute;background:radial-gradient(ellipse,rgba(0,0,0,.9) 40%,transparent 72%)}

.marquee{font-family:"Russo One",sans-serif;color:var(--white);
  text-shadow:0 0 6px rgba(255,255,255,.9),0 0 18px rgba(255,230,200,.6)}
.headline{top:305px;font-size:78px;letter-spacing:2px}
.subhead{top:387px;font-size:38px;color:#eee}
.dates{top:456px;font-family:"Russo One",sans-serif;font-size:27px;letter-spacing:1px}

.style-salsa{font-family:"Archivo Black",sans-serif;color:var(--red-text);text-shadow:0 0 6px rgba(229,34,28,.6)}
.style-bachata{font-family:"Archivo Black",sans-serif;color:var(--silver);letter-spacing:10px}
.style-kizomba{font-family:"Archivo Black",sans-serif;color:var(--gold);text-shadow:0 0 5px rgba(227,181,66,.5)}

.perks{position:absolute;left:292px;width:196px;top:550px;text-align:center;font-family:"Rajdhani",sans-serif;font-weight:700;white-space:nowrap}
.perks__lead{color:var(--red-text);font-size:23px;line-height:23px}
.perks__item{font-size:23px;line-height:23px}
.perks__item--small{font-size:21px;line-height:24px}
.perks__item--gap{margin-top:6px}

.contact{position:absolute;top:669px;left:0;right:0;display:flex;justify-content:center;gap:12px;font-size:14.5px;font-weight:600;letter-spacing:.5px;white-space:nowrap}
.contact__item{display:flex;align-items:center;gap:5px}
.contact__icon{width:11px;height:11px}
.contact__dot{width:10px;height:10px;border-radius:50%;background:var(--red-text)}

.offer-ring{position:absolute;left:176px;top:124px;width:170px;height:170px;border-radius:50%;
  background:radial-gradient(circle,rgba(20,8,18,.8) 55%,rgba(120,30,50,.4) 70%,transparent 72%)}
.offer{font-family:"Russo One",sans-serif;text-align:center}
.offer__top{top:165px;font-size:34px}
.offer__mid{top:202px;font-size:22px}
.offer__bottom{top:225px;font-size:32px;color:var(--silver)}
.schedule-title{top:263px;font-size:60px;letter-spacing:1px}

.schedule{position:absolute;top:329px;left:26px;display:flex;gap:17px}
.day{width:139px}
.day__name{height:26px;background:var(--panel);border-radius:4px;text-align:center;
  font-family:"Russo One",sans-serif;color:var(--yellow);font-size:19px;line-height:26px;white-space:nowrap}
.day__slots{margin-top:6px;height:72px;background:var(--panel);border-radius:4px;
  list-style:none;padding-top:5px;text-align:center;font-size:15px;font-weight:500;line-height:21px;color:#e8e8e8}

.rule{position:absolute;left:170px;width:170px;top:622px;height:1px;background:linear-gradient(90deg,transparent,var(--silver),transparent)}
.venue{top:631px;font-family:"Russo One",sans-serif;font-size:27px;color:#eee}
</style>
</head>
<body>

<section class="flyer flyer--front" aria-label="Flyer voorzijde">
  <div class="photo photo--couple" role="img" aria-label="Foto van een dansend salsapaar in een dip"></div>

  <div class="brand" style="left:0"><span class="brand__dot"></span><span class="brand__name">SOLARA</span></div>
  <p class="brand__tag" style="left:0">FEEL THE RHYTHM, MOVE TOGETHER</p>

  <div class="splash" style="left:60px;top:300px;width:420px;height:200px"></div>
  <h1 class="abs center marquee headline">GRATIS</h1>
  <p class="abs center marquee subhead">PROEFLESSEN</p>
  <p class="abs center dates">26 T/M 28 SEPT</p>

  <div class="splash" style="left:0;top:520px;width:300px;height:150px;opacity:.6"></div>
  <p class="abs style-salsa" style="left:28px;top:524px;font-size:58px">SALSA</p>
  <p class="abs style-bachata" style="left:32px;top:584px;font-size:33px">BACHATA</p>
  <p class="abs style-kizomba" style="left:30px;top:619px;font-size:46px">KIZOMBA</p>

  <div class="perks">
    <p class="perks__lead">EERSTE LES GRATIS</p>
    <p class="perks__item">STUDENTE KORTING</p>
    <p class="perks__item perks__item--small perks__item--gap">ELK NIVEAU</p>
    <p class="perks__item perks__item--small">ALLE LEEFTIJDEN</p>
  </div>

  <div class="contact">
    <span class="contact__item"><svg class="contact__icon" viewBox="0 0 10 10"><path d="M5 0a3.5 3.5 0 0 0-3.5 3.5C1.5 6 5 10 5 10s3.5-4 3.5-6.5A3.5 3.5 0 0 0 5 0z" fill="#e5221c"/><circle cx="5" cy="3.5" r="1.3" fill="#fff"/></svg>KADE 4, 1011 AB ZANDHOVEN</span>
    <span class="contact__item"><svg class="contact__icon" viewBox="0 0 10 10"><circle cx="5" cy="5" r="5" fill="#e5221c"/><path d="M3 2.5l1 1-.5.8c.4.8 1 1.4 1.8 1.8l.8-.5 1 1-.6.9C4.8 7.2 2.8 5.2 2.5 3.3z" fill="#fff"/></svg>0612345678</span>
    <span class="contact__item"><span class="contact__dot"></span>SOLARADANS</span>
  </div>
</section>

<section class="flyer flyer--back" aria-label="Flyer achterzijde">
  <div class="brand" style="left:147px"><span class="brand__dot"></span><span class="brand__name">SOLARA</span></div>
  <p class="brand__tag" style="left:147px">FEEL THE RHYTHM, MOVE TOGETHER</p>

  <div class="offer-ring"></div>
  <p class="abs center offer offer__top">ALTIJD</p>
  <p class="abs center offer offer__mid">EERSTE LES</p>
  <p class="abs center offer offer__bottom">GRATIS</p>
  <h2 class="abs center marquee schedule-title">LES ROOSTER</h2>

  <div class="schedule">
    <div class="day"><p class="day__name">DINSDAG</p>
      <ul class="day__slots"><li>19:00 Salsa 1</li><li>20:00 Salsa 3</li><li>21:00 Bachata 3</li></ul></div>
    <div class="day"><p class="day__name">WOENSDAG</p>
      <ul class="day__slots"><li>19:00 Kizomba 2</li><li>20:00 Kizomba 1</li><li>21:00 Kizomba 3</li></ul></div>
    <div class="day"><p class="day__name">DONDERDAG</p>
      <ul class="day__slots"><li>19:00 Salsa 2</li><li>20:00 Bachata 1</li><li>21:00 Bachata 2</li></ul></div>
  </div>

  <div class="splash" style="left:60px;top:430px;width:380px;height:230px;opacity:.7"></div>
  <div class="photo photo--pair" role="img" aria-label="Foto van een salsapaar in dansvoering"></div>
  <p class="abs style-salsa" style="left:170px;top:450px;font-size:62px">SALSA</p>
  <p class="abs style-bachata" style="left:164px;top:516px;font-size:36px">BACHATA</p>
  <p class="abs style-kizomba" style="left:152px;top:555px;font-size:50px">KIZOMBA</p>

  <div class="rule"></div>
  <p class="abs venue" style="left:0;width:470px;text-align:center">CLUB MERIDIA</p>

  <div class="contact">
    <span class="contact__item"><svg class="contact__icon" viewBox="0 0 10 10"><path d="M5 0a3.5 3.5 0 0 0-3.5 3.5C1.5 6 5 10 5 10s3.5-4 3.5-6.5A3.5 3.5 0 0 0 5 0z" fill="#e5221c"/><circle cx="5" cy="3.5" r="1.3" fill="#fff"/></svg>KADE 4, 1011 AB ZANDHOVEN</span>
    <span class="contact__item"><svg class="contact__icon" viewBox="0 0 10 10"><circle cx="5" cy="5" r="5" fill="#e5221c"/><path d="M3 2.5l1 1-.5.8c.4.8 1 1.4 1.8 1.8l.8-.5 1 1-.6.9C4.8 7.2 2.8 5.2 2.5 3.3z" fill="#fff"/></svg>0612345678</span>
    <span class="contact__item"><span class="contact__dot"></span>SOLARADANS</span>
  </div>
</section>

</body>
</html>
```